Clearpath Ledger Billing Company Business card

Need a business card that stands out that includes name of company,(above) Owners name Marisol Whitfield phone#555-314-7762 email# ClearpathLedgerBC@mailbox-example.com and website www.Clearpathledgerbillingcompany-example.com. This is a medical billing company so the card has to relate to that or relate to steady cashflow

```html
<!DOCTYPE html>
<html lang="en">
<head>
<meta charset="utf-8">
<title>Clearpath Ledger Billing Company – Business Card</title>
<link rel="stylesheet" href="https://fonts.googleapis.com/css2?family=Roboto:ital,wght@0,400;0,500;1,400&family=Roboto+Condensed:wght@400&display=swap">
<style>
  :root {
    --page-bg: #e8e5e0;
    --card-bg: #f5f7f8;
    --brand-blue: #1f5ea8;
    --deep-blue: #1d4f8f;
    --brand-green: #7cc242;
    --text-blue: #1e4a86;
    --name-white: #f2f5fa;
  }
  html, body {
    margin: 0;
    width: 1200px;
    height: 1200px;
    overflow: hidden;
    background: var(--page-bg);
  }
  .canvas {
    position: relative;
    width: 1200px;
    height: 1200px;
    display: flex;
    align-items: center;
    justify-content: center;
  }
  .business-card {
    width: 1040px;
    height: 617px;
    box-shadow: 0 10px 30px rgba(0,0,0,0.15);
    display: block;
  }
  .card-face { fill: var(--card-bg); }
  .header-band { fill: var(--brand-blue); }
  .accent-line, .contact-icon { fill: var(--brand-green); }
  .owner-name {
    font-family: "Roboto Condensed", "Arial Narrow", sans-serif;
    font-size: 30px;
    fill: var(--name-white);
  }
  .owner-title {
    font-family: "Roboto", Arial, sans-serif;
    font-style: italic;
    font-size: 18px;
    fill: var(--name-white);
  }
  .contact-text {
    font-family: "Roboto", Arial, sans-serif;
    font-size: 20px;
    fill: var(--text-blue);
  }
  .company-name {
    font-family: "Roboto", Arial, sans-serif;
    font-weight: 500;
    font-size: 30px;
    letter-spacing: 1.5px;
    fill: var(--deep-blue);
  }
  .company-mark { fill: var(--brand-green); }
</style>
</head>
<body>
<main class="canvas">
  <svg class="business-card" viewBox="0 0 860 510" xmlns="http://www.w3.org/2000/svg" aria-label="Clearpath Ledger Billing Company business card">
    <rect class="card-face" x="0" y="0" width="860" height="510"/>

    <!-- header band with straight diagonal edge and parallel accent line -->
    <polygon class="header-band" points="0,0 860,0 860,190 0,30"/>
    <polygon class="accent-line" points="0,42 860,202 860,212 0,52"/>

    <!-- owner -->
    <text class="owner-name" x="812" y="85" text-anchor="end">Marisol Whitfield</text>
    <text class="owner-title" x="810" y="117" text-anchor="end">Owner</text>

    <!-- contact details -->
    <g class="contact-row">
      <path class="contact-icon" d="M86,168 h22 a2,2 0 0 1 2,2 v3 h-6 v-2 h-14 v2 h-6 v-3 a2,2 0 0 1 2,-2 Z M90,175 h14 l4,8 v3 h-22 v-3 Z"/>
      <text class="contact-text" x="127" y="183">555-314-7762</text>
    </g>
    <g class="contact-row">
      <rect class="contact-icon" x="86" y="204" width="20" height="14" rx="1"/>
      <path d="M86,205 L96,213 L106,205" fill="none" stroke="#f5f7f8" stroke-width="1.6"/>
      <text class="contact-text" x="127" y="218">ClearpathLedgerBC@mailbox-example.com</text>
    </g>
    <g class="contact-row">
      <circle class="contact-icon" cx="96" cy="245" r="9"/>
      <path d="M87,245 h18 M96,236 v18" fill="none" stroke="#f5f7f8" stroke-width="1.1"/>
      <text class="contact-text" x="127" y="252">Clearpathledgerbillingcompany-example.com</text>
    </g>

    <!-- company name -->
    <rect class="company-mark" x="40" y="354" width="44" height="44"/>
    <text class="company-name" x="104" y="372">CLEARPATH LEDGER</text>
    <text class="company-name" x="104" y="406">BILLING COMPANY</text>
  </svg>
</main>
</body>
</html>
```